Road Construction Company needs business cards

We would like a new business card designed for our business.

We're a road construction company based in Qld, Australia.

Can the business card please have the following information on it.

Name: Brent Halloway
Position: General Manager
Phone: 0491 257 314
Email: Brent.halloway@drovik.com.au
Address: 87 Margrove Ave, Tindale, QLD, 4016
Website: www.drovik.com.au

Visually we'd like the card to be professional and simple.

Attached is our logo.

Our website is www.drovik.com.au

Target Market(s)

Men aged 25-60

Contact Information for Business Card

As listed in project description

Font styles to use
Serif

Requirements
Must have
• Large logo on back of card

```html
<!DOCTYPE html>
<html lang="en">
<head>
<meta charset="utf-8">
<title>Drovik Business Card</title>
<link href="https://fonts.googleapis.com/css2?family=Lato:wght@400;700;900&display=swap" rel="stylesheet">
<style>
  :root {
    --stage: #2a2a2a;
    --brand-blue: #0556a3;
    --ink-blue: #0a4fa0;
    --sky-blue: #2f9bd8;
    --pale-band: #e7eef7;
    --paper: #ffffff;
    --text: #1f1f1f;
  }
  * { margin: 0; padding: 0; box-sizing: border-box; }
  html, body {
    width: 1200px; height: 875px; overflow: hidden;
    background: var(--stage);
    font-family: "Lato", Arial, sans-serif;
  }
  .canvas {
    position: relative; width: 1200px; height: 875px;
    display: flex; flex-direction: column; align-items: center; justify-content: center; gap: 40px;
  }
  .card {
    position: relative; width: 680px; height: 388px;
    border-radius: 22px; overflow: hidden;
  }
  /* Back */
  .card-back {
    background: var(--brand-blue);
    display: flex; align-items: center; justify-content: center;
  }
  .card-back .wordmark {
    color: var(--paper); font-weight: 900; font-size: 104px; letter-spacing: 6px;
  }
  /* Front */
  .card-front { background: var(--paper); }
  .card-front .decor { position: absolute; inset: 0; }
  .card-front .wordmark {
    position: absolute; top: 34px; right: 42px;
    color: var(--ink-blue); font-weight: 900; font-size: 62px; letter-spacing: 3px;
  }
  .rule-top {
    position: absolute; top: 122px; left: 300px; right: 28px;
    height: 1px; background: var(--sky-blue);
  }
  .address {
    position: absolute; top: 150px; right: 40px;
    text-align: right; font-size: 16px; line-height: 1.5; color: var(--text);
  }
  .person { position: absolute; left: 46px; top: 208px; }
  .person .name {
    color: var(--ink-blue); font-weight: 900; font-size: 31px; text-transform: uppercase; letter-spacing: 0.2px;
  }
  .person .role { color: var(--sky-blue); font-size: 20px; margin-top: 2px; }
  .rule-person {
    position: absolute; left: 46px; top: 283px; width: 270px; height: 1px; background: var(--sky-blue);
  }
  .contacts { position: absolute; left: 46px; top: 296px; list-style: none; }
  .contacts li {
    display: flex; align-items: center; gap: 10px;
    font-size: 15px; line-height: 22px; color: var(--text);
  }
  .contacts svg { width: 14px; height: 14px; fill: var(--ink-blue); flex: none; }
</style>
</head>
<body>
<main class="canvas">
  <section class="card card-back" aria-label="Card back">
    <div class="wordmark">DROVIK</div>
  </section>

  <section class="card card-front" aria-label="Card front">
    <svg class="decor" viewBox="0 0 680 388" preserveAspectRatio="none" aria-hidden="true">
      <polygon points="120,120 300,120 560,388 330,388" fill="var(--pale-band)"/>
      <polygon points="0,372 520,372 506,388 0,388" fill="var(--brand-blue)"/>
      <polygon points="538,340 680,340 680,388 522,388" fill="var(--sky-blue)"/>
    </svg>

    <div class="wordmark">DROVIK</div>
    <div class="rule-top"></div>

    <address class="address" style="font-style:normal">
      87 Margrove Ave<br>Tindale, QLD, 4016
    </address>

    <div class="person">
      <div class="name">Brent Halloway</div>
      <div class="role">General Manager</div>
    </div>
    <div class="rule-person"></div>

    <ul class="contacts">
      <li>
        <svg viewBox="0 0 24 24"><path d="M6.6 10.8a15.1 15.1 0 0 0 6.6 6.6l2.2-2.2a1 1 0 0 1 1-.25 11.4 11.4 0 0 0 3.6.57 1 1 0 0 1 1 1V20a1 1 0 0 1-1 1A17 17 0 0 1 3 4a1 1 0 0 1 1-1h3.5a1 1 0 0 1 1 1c0 1.25.2 2.45.57 3.57a1 1 0 0 1-.25 1z"/></svg>
        0491 257 314
      </li>
      <li>
        <svg viewBox="0 0 24 24"><path d="M2 5h20v14H2zm2 2v.5l8 5 8-5V7l-8 5z"/></svg>
        Brent.halloway@drovik.com.au
      </li>
      <li>
        <svg viewBox="0 0 24 24"><path d="M12 2a10 10 0 1 0 0 20 10 10 0 0 0 0-20zm6.9 9h-3a15 15 0 0 0-1.3-5.6A8 8 0 0 1 18.9 11zM12 4.1c.9 1.3 1.8 3.6 1.9 6.9h-3.8c.1-3.3 1-5.6 1.9-6.9zM9.4 5.4A15 15 0 0 0 8.1 11h-3a8 8 0 0 1 4.3-5.6zM5.1 13h3a15 15 0 0 0 1.3 5.6A8 8 0 0 1 5.1 13zm6.9 6.9c-.9-1.3-1.8-3.6-1.9-6.9h3.8c-.1 3.3-1 5.6-1.9 6.9zm2.6-1.3a15 15 0 0 0 1.3-5.6h3a8 8 0 0 1-4.3 5.6z"/></svg>
        www.drovik.com.au
      </li>
    </ul>
  </section>
</main>
</body>
</html>
```